No Credit Score QT and ZMR

I'm looking for a banner to display on emails as well as facebook. The facebook banner would need to be square and the other size is 728 x 90. We are a mortgage company that does mostly Military home loans. We would like to start out with just this banner, then do about 20 others once we find the right designer. I need something simple but that stands out. Our company website is www.harborpeakfinancial.com. The text for this will be ( Ask about our "No Credit Score" program for ZMR and QT)

```html
<!DOCTYPE html>
<html lang="en">
<head>
<meta charset="utf-8">
<title>No Credit Score Program – Military Home Loans</title>
<link href="https://fonts.googleapis.com/css2?family=Quicksand:wght@400;700&family=Montserrat:wght@400;700&family=Open+Sans:wght@300&family=Arimo:wght@400;700&display=swap" rel="stylesheet">
<style>
  :root{
    --brand-blue:#2e78b8;
    --light-blue:#4aa6dc;
    --title-blue:#2f6db5;
    --navy-line:#3346a6;
    --charcoal:#2a2a2a;
    --offer-red:#e8202a;
    --tail-red:#b0262b;
    --shadow-grey:#8a8a8a;
    --ink:#222;
    --white:#fff;
  }
  html,body{margin:0;padding:0;overflow:hidden;background:var(--white);}
  .banner{display:block;width:1200px;height:1200px;}
  .url{font-family:"Open Sans",sans-serif;font-weight:300;font-size:30px;fill:var(--white);}
  .headline-strong{font-family:"Quicksand",sans-serif;font-weight:700;font-size:104px;fill:var(--title-blue);}
  .headline-light{font-family:"Quicksand",sans-serif;font-weight:400;font-size:112px;fill:var(--title-blue);}
  .program-line{font-family:"Arimo",sans-serif;font-size:62px;fill:var(--ink);}
  .badge-strong{font-family:"Montserrat",sans-serif;font-weight:700;font-size:56px;fill:var(--white);letter-spacing:2px;}
  .badge-light{font-family:"Montserrat",sans-serif;font-weight:400;font-size:50px;fill:var(--white);}
  .corner-small{font-family:"Arimo",sans-serif;font-weight:700;font-size:30px;fill:var(--white);}
  .corner-large{font-family:"Arimo",sans-serif;font-weight:400;font-size:52px;fill:var(--white);}
  .corner-pct{font-family:"Arimo",sans-serif;font-weight:700;font-size:56px;fill:var(--white);}
  .bubble-text{font-family:"Montserrat",sans-serif;font-weight:700;fill:var(--white);}
  .cta-text{font-family:"Montserrat",sans-serif;font-weight:700;fill:var(--brand-blue);}
  .dash-line{fill:none;stroke:#444;stroke-width:2;stroke-dasharray:14 10;}
  .frame-line{fill:none;stroke:var(--navy-line);stroke-width:6;}
</style>
</head>
<body>
<svg class="banner" viewBox="0 0 1500 1500" xmlns="http://www.w3.org/2000/svg">
  <defs>
    <linearGradient id="photoTone" x1="0" y1="0" x2="0" y2="1">
      <stop offset="0" stop-color="#b8c4d0"/>
      <stop offset="0.3" stop-color="#e2e0da"/>
      <stop offset="0.55" stop-color="#d6d0c2"/>
      <stop offset="0.78" stop-color="#a3b27a"/>
      <stop offset="0.9" stop-color="#7f9d4e"/>
      <stop offset="1" stop-color="#c7b79a"/>
    </linearGradient>
    <radialGradient id="photoWarm" cx="0.55" cy="0.55" r="0.4">
      <stop offset="0" stop-color="#9aa6b4" stop-opacity="0.55"/>
      <stop offset="0.6" stop-color="#c9b19a" stop-opacity="0.25"/>
      <stop offset="1" stop-color="#c9b19a" stop-opacity="0"/>
    </radialGradient>
    <linearGradient id="badgeFill" x1="0" y1="0" x2="1" y2="0">
      <stop offset="0" stop-color="#3568b8"/>
      <stop offset="1" stop-color="#3f52a8"/>
    </linearGradient>
  </defs>

  <!-- hero photo area -->
  <g class="hero-photo" role="img" aria-label="Photo of a military family – a soldier in uniform, his wife and four young boys – standing on the lawn in front of their new two-storey house">
    <polygon points="0,0 960,0 1210,410 930,880 160,880 0,520" fill="url(#photoTone)"/>
    <polygon points="0,0 960,0 1210,410 930,880 160,880 0,520" fill="url(#photoWarm)"/>
  </g>

  <!-- left accent wedges -->
  <polygon points="0,430 200,880 150,880 0,540" fill="var(--light-blue)"/>
  <polygon points="0,540 150,880 0,880" fill="var(--brand-blue)"/>

  <!-- right dark panel and chevron -->
  <polygon points="1050,0 1500,0 1500,540 1330,880 1020,880 1300,410" fill="var(--charcoal)"/>
  <polygon points="960,0 1050,0 1300,410 1020,880 930,880 1210,410" fill="var(--brand-blue)"/>
  <polygon points="1500,540 1500,640 1370,1060 1290,1060" fill="var(--brand-blue)"/>

  <!-- website band -->
  <polygon class="web-band" points="150,880 1380,880 1330,1060 0,1060 0,1020" fill="var(--brand-blue)"/>
  <g class="globe-icon" fill="none" stroke="var(--white)" stroke-width="4">
    <circle cx="202" cy="970" r="31"/>
    <ellipse cx="202" cy="970" rx="13" ry="31"/>
    <line x1="171" y1="970" x2="233" y2="970"/>
    <line x1="176" y1="954" x2="228" y2="954"/>
    <line x1="176" y1="986" x2="228" y2="986"/>
  </g>
  <text class="url" x="270" y="980">www.harborpeakfinancial.com</text>

  <!-- headline -->
  <text class="headline-strong" x="38" y="1196">Military home</text>
  <text class="headline-light" x="40" y="1318">loans.</text>
  <text class="program-line" x="38" y="1415">Program For ZMR and QT</text>

  <!-- no credit score badge -->
  <polygon points="995,162 1068,62 1500,62 1500,264 1068,264" fill="#d8d8d8"/>
  <polygon points="1006,162 1074,70 1500,70 1500,248 1074,248" fill="url(#badgeFill)"/>
  <text class="badge-strong" x="1072" y="146">NO CREDIT</text>
  <text class="badge-light" x="1090" y="212">SCORE</text>

  <!-- corner ribbon -->
  <polygon class="corner-ribbon" points="0,300 300,0 430,0 0,430" fill="var(--offer-red)"/>
  <g transform="translate(40,290) rotate(-45)">
    <text class="corner-small" x="0" y="0">Military home</text>
    <text class="corner-large" x="200" y="0">loans.</text>
    <text class="corner-pct" x="205" y="52">25<tspan font-size="30" font-weight="400">%</tspan></text>
  </g>

  <!-- offer bubble -->
  <polyline class="dash-line" points="795,1050 800,945 1240,870 1330,905"/>
  <polyline class="frame-line" points="800,960 1090,900"/>
  <polyline class="dash-line" points="900,1470 978,1300 810,1245"/>
  <polyline class="frame-line" points="765,1070 765,1245 900,1280"/>
  <polyline class="frame-line" points="1340,990 1420,1200 1350,1240 1350,1395 1170,1350"/>
  <polyline class="dash-line" points="1400,1215 1425,1270 1340,1255"/>
  <polyline class="dash-line" points="1120,1335 960,1440"/>

  <polygon points="840,1200 1360,1170 1300,1340 1040,1300" fill="var(--shadow-grey)"/>
  <polygon points="990,1370 1170,1215 1060,1230" fill="var(--tail-red)"/>
  <polygon points="820,985 1225,910 1305,1262 805,1222" fill="var(--offer-red)"/>
  <polygon points="1060,1015 1305,945 1365,1175 1075,1168" fill="var(--white)"/>

  <text class="bubble-text" font-size="34" transform="translate(838,1032) rotate(-13)">YOU THINK</text>
  <text class="bubble-text" font-size="34" transform="translate(898,1065) rotate(-13)">WE GIVE</text>
  <text class="cta-text" font-size="36" transform="translate(1078,1062) rotate(-12)">GET</text>
  <text class="cta-text" font-size="42" transform="translate(1132,1095) rotate(-12)">STARTED</text>
  <text class="cta-text" font-size="42" transform="translate(1212,1126) rotate(-12)">NOW</text>
  <text class="bubble-text" font-size="42" transform="translate(848,1198) rotate(5)">SUPREME OFFER</text>
</svg>
</body>
</html>
```